Business Card for Trivelo, a french tech company

Tech company
New technologies
Serious design
Dark theme

User info :
Name: Florian GASTIER
Position: Co-Founder & CEO
Tel: (+33) 6 52 84 26 07
Email: florian@trivelo.example
Website: www.trivelo.example
Address: 17 rue des Tanneurs 31000 TOULOUSE

```html
<!DOCTYPE html>
<html lang="fr">
<head>
<meta charset="utf-8">
<title>Trivelo – Business Card</title>
<link rel="stylesheet" href="https://fonts.googleapis.com/css2?family=Josefin+Sans:wght@400;700&display=swap">
<style>
  :root {
    --page: #ece9e4;
    --card: #05031f;
    --magenta: #c4268f;
    --violet: #7a4cb8;
    --teal: #1f7291;
    --white: #f4f2fa;
    --shadow: rgba(10, 6, 30, 0.35);
  }
  * { margin: 0; padding: 0; box-sizing: border-box; }
  html, body {
    width: 1200px;
    height: 900px;
    overflow: hidden;
    background: var(--page);
    font-family: "Josefin Sans", sans-serif;
  }
  .sheet {
    width: 1200px;
    height: 900px;
    display: flex;
    flex-direction: column;
    align-items: center;
    justify-content: center;
    gap: 44px;
  }
  .card {
    position: relative;
    width: 630px;
    height: 360px;
    background: var(--card);
    border-radius: 34px;
    box-shadow: 0 14px 30px var(--shadow);
    overflow: hidden;
    color: var(--white);
  }

  /* Back side */
  .card-back .brand {
    position: absolute;
    top: 128px;
    left: 0;
    width: 100%;
    display: flex;
    align-items: center;
    justify-content: center;
    gap: 12px;
  }
  .brand-dot {
    width: 16px;
    height: 16px;
    border-radius: 50%;
    background: var(--magenta);
  }
  .brand-name {
    font-weight: 700;
    font-size: 36px;
    letter-spacing: 2px;
    color: var(--teal);
  }
  .card-back .rule {
    position: absolute;
    top: 196px;
    left: 150px;
    width: 330px;
    height: 1px;
    background: linear-gradient(90deg, transparent, var(--magenta) 50%, transparent);
  }
  .card-back .site {
    position: absolute;
    top: 212px;
    left: 0;
    width: 100%;
    text-align: center;
    font-weight: 700;
    font-size: 15px;
    letter-spacing: 6px;
    color: var(--teal);
  }

  /* Front side */
  .wordmark {
    position: absolute;
    top: 36px;
    left: 38px;
    font-weight: 700;
    font-size: 78px;
    letter-spacing: 3px;
    line-height: 1;
    color: var(--magenta);
  }
  .identity {
    position: absolute;
    right: 330px;
    bottom: 52px;
    text-align: right;
  }
  .identity .role {
    font-size: 17px;
    color: var(--white);
  }
  .identity .name {
    margin-top: 4px;
    font-size: 19px;
    color: var(--violet);
  }
  .divider {
    position: absolute;
    left: 315px;
    bottom: 40px;
    width: 1px;
    height: 100px;
    background: linear-gradient(180deg, transparent, var(--magenta) 50%, transparent);
  }
  .contact {
    position: absolute;
    left: 330px;
    bottom: 44px;
    list-style: none;
    font-size: 14px;
    line-height: 24px;
    color: var(--white);
  }
  .contact li {
    display: flex;
    align-items: center;
    gap: 9px;
    white-space: nowrap;
  }
  .contact svg {
    width: 14px;
    height: 14px;
    flex: none;
    fill: none;
    stroke: var(--violet);
    stroke-width: 1.8;
    stroke-linecap: round;
    stroke-linejoin: round;
  }
</style>
</head>
<body>
<main class="sheet">

  <section class="card card-back" aria-label="Verso de la carte">
    <div class="brand">
      <span class="brand-dot"></span>
      <span class="brand-name">Trivelo</span>
    </div>
    <div class="rule"></div>
    <p class="site">www.trivelo.example</p>
  </section>

  <section class="card card-front" aria-label="Recto de la carte">
    <h1 class="wordmark">TRIVELO</h1>

    <div class="identity">
      <p class="role">Co-Founder &amp; CEO</p>
      <p class="name">Florian GASTIER</p>
    </div>

    <div class="divider"></div>

    <ul class="contact">
      <li>
        <svg viewBox="0 0 24 24"><path d="M5 3h4l2 5-2.5 1.5a11 11 0 0 0 6 6L16 13l5 2v4a2 2 0 0 1-2 2A16 16 0 0 1 3 5a2 2 0 0 1 2-2z"/></svg>
        (+33) 6 52 84 26 07
      </li>
      <li>
        <svg viewBox="0 0 24 24"><rect x="3" y="5" width="18" height="14" rx="1"/><path d="M3 6l9 7 9-7"/></svg>
        florian@trivelo.example
      </li>
      <li>
        <svg viewBox="0 0 24 24"><circle cx="12" cy="12" r="9"/><path d="M3 12h18M12 3a14 14 0 0 1 0 18M12 3a14 14 0 0 0 0 18"/></svg>
        www.trivelo.example
      </li>
      <li>
        <svg viewBox="0 0 24 24"><path d="M12 22s7-7 7-12a7 7 0 0 0-14 0c0 5 7 12 7 12z"/><circle cx="12" cy="10" r="2.5"/></svg>
        17 rue des Tanneurs 31000 TOULOUSE
      </li>
    </ul>
  </section>

</main>
</body>
</html>
```